Verdant Orchard - Stationery Design Project

We need a stationary for our business. We grow roots and fruits in Central and South America, we import and distribute in FL, USA. We do fresh and frozen products.

Target Market(s)

Small and big supermarkets, wholesalers, traders, distributors, etc

Industry/Entity Type

Business

```html
<!DOCTYPE html>
<html lang="en">
<head>
<meta charset="utf-8">
<title>Verdant Orchard Stationery</title>
<link rel="stylesheet" href="https://fonts.googleapis.com/css2?family=Open+Sans:wght@400;600&family=Tinos:ital@0;1&display=swap">
<style>
  :root {
    --backdrop: #e4e4e4;
    --paper: #ffffff;
    --card: #fbfbfb;
    --leaf-green: #55643a;
    --leaf-pale: #dcded6;
    --orange: #e07a12;
    --ink: #111111;
    --muted: #555555;
  }
  * { margin: 0; padding: 0; box-sizing: border-box; }
  html, body { width: 1200px; height: 1000px; overflow: hidden; }
  body {
    position: relative;
    background: var(--backdrop);
    font-family: "Open Sans", Arial, sans-serif;
  }
  .sheet, .card { position: absolute; overflow: hidden; }

  /* Brand name lockup */
  .brand { display: flex; align-items: center; justify-content: center; gap: 6px; }
  .brand-dot { width: 8px; height: 8px; border-radius: 50%; background: var(--leaf-green); }
  .brand-name {
    font-family: "Open Sans", Arial, sans-serif;
    font-weight: 600;
    color: var(--leaf-green);
    letter-spacing: 0.5px;
    text-transform: uppercase;
    white-space: nowrap;
  }

  /* Letterhead */
  .letterhead { left: 85px; top: 75px; width: 602px; height: 850px; background: var(--paper); }
  .letterhead .brand { position: absolute; top: 66px; left: 0; right: 0; }
  .letterhead .brand-name { font-size: 17px; }
  .letter {
    position: absolute; left: 78px; top: 194px; width: 449px;
    font-family: "Tinos", "Times New Roman", serif;
    font-size: 12.6px; line-height: 15.8px; color: var(--ink);
  }
  .letter p { text-align: justify; margin-bottom: 16px; }
  .letter .salutation { margin-bottom: 16px; }
  .letter .closing { margin-top: 58px; margin-bottom: 0; text-align: left; }
  .signature { width: 108px; height: 30px; margin: 6px 0 4px; background: #dedede; border-radius: 3px; }
  .letter .signer { text-align: left; }

  .letter-footer {
    position: absolute; left: 75px; top: 754px;
    font-size: 6.5px; line-height: 10.6px; color: var(--muted);
  }
  .letter-footer .address { margin-bottom: 4px; }
  .contact-row { display: flex; align-items: center; gap: 8px; }
  .icon { width: 7px; height: 7px; flex: none; }

  .corner-motif {
    position: absolute; border-radius: 50%;
  }
  .letterhead .corner-motif { width: 190px; height: 190px; right: -60px; bottom: -70px; background: var(--leaf-green); }

  /* Business cards */
  .card { left: 722px; width: 389px; height: 216px; background: var(--card); }
  .card-front { top: 74px; }
  .card-front .brand { position: absolute; top: 98px; left: 0; right: 0; }
  .card-front .brand-name { font-size: 20px; }
  .card-front .website {
    position: absolute; top: 144px; left: 0; right: 0; text-align: center;
    font-size: 12px; color: var(--leaf-green); letter-spacing: 0.4px;
  }
  .card-back { top: 318px; }
  .card-back .brand { position: absolute; top: 44px; left: 36px; justify-content: flex-start; }
  .card-back .brand-name { font-size: 16px; }
  .card-back .corner-motif { width: 200px; height: 200px; right: -60px; bottom: -90px; background: var(--leaf-pale); }
  .person { position: absolute; left: 36px; top: 107px; }
  .person-name { font-size: 13.5px; color: var(--leaf-green); letter-spacing: 0.3px; }
  .person-role { font-size: 7.5px; color: var(--orange); margin-top: 3px; }
  .card-contact { position: absolute; left: 31px; top: 155px; font-size: 7.5px; color: var(--muted); }
  .card-contact .address { margin-bottom: 8px; letter-spacing: 0.2px; }
  .card-contact .grid { display: grid; grid-template-columns: 105px auto; row-gap: 4px; }
</style>
</head>
<body>

<svg width="0" height="0" style="position:absolute">
  <defs>
    <symbol id="i-mobile" viewBox="0 0 10 10"><rect x="3" y="0.5" width="4" height="9" rx="0.8" fill="none" stroke="#e07a12" stroke-width="1"/></symbol>
    <symbol id="i-phone" viewBox="0 0 10 10"><path d="M1 4 Q5 0 9 4 L8 5 L6.5 4 L3.5 4 L2 5 Z M2.5 6 H7.5 V9 H2.5 Z" fill="#e07a12"/></symbol>
    <symbol id="i-fax" viewBox="0 0 10 10"><rect x="3" y="0.8" width="4" height="3" fill="none" stroke="#e07a12"/><rect x="1" y="4" width="8" height="4.5" fill="#e07a12"/></symbol>
    <symbol id="i-mail" viewBox="0 0 10 10"><rect x="0.8" y="2" width="8.4" height="6" fill="none" stroke="#e07a12"/><path d="M1 2.3 L5 5.5 L9 2.3" fill="none" stroke="#e07a12"/></symbol>
    <symbol id="i-web" viewBox="0 0 10 10"><circle cx="5" cy="5" r="4.2" fill="#e07a12"/><path d="M1 5 H9 M5 1 V9" stroke="#fff" stroke-width="0.7"/></symbol>
  </defs>
</svg>

<section class="sheet letterhead">
  <div class="brand"><span class="brand-dot"></span><span class="brand-name">Verdant Orchard</span></div>

  <div class="letter">
    <p class="salutation">Gentlemen,</p>
    <p>Enclosed I have the honor to send you an article which I should be pleased if you would accept for the "Meridian Review". I am <i>desperately</i> pushed for money; and in the event of Mr. Whitcombe's liking the "Landscape-Garden", I would take it as an especial favor if you would mail me the amount due for it, so as to reach me here by the 21st, on which day I shall need it. Can you possibly oblige me in this? If you accept the paper I presume you will allow me your usual sum, whatever that is for similar contributions—but I set no price—leaving all to your own liberality. The piece will make 8 of your pages and rather more.</p>
    <p>Will you be kind enough to put the best possible interpretation upon my behavior while in N-York? You must have conceived a <i>queer</i> idea of me—but the simple truth is that Ransome would insist upon <i>the juleps</i>, and I knew not what I was either doing or saying. The Review of Linford which I offered you was deficient in a 1/2 page of commencement, which I had written to supersede the old beginning, and which gave the article the character of a general and retrospective review. No wonder you did not take it—I would have been very much mortified if you had. I hope to see you at some future time, under better auspices.</p>
    <p class="closing">In the meantime I remain<br>Yours very truly,</p>
    <div class="signature" role="img" aria-label="Handwritten signature of the sender"></div>
    <p class="signer">Elias Hartwell</p>
  </div>

  <div class="letter-footer">
    <div class="address">#2 Palm Grove Lane, Miami, FL 33101, USA</div>
    <div class="contact-row"><svg class="icon"><use href="#i-mobile"/></svg>+1 305 555 0148</div>
    <div class="contact-row"><svg class="icon"><use href="#i-phone"/></svg>+1 305 555 0177</div>
    <div class="contact-row"><svg class="icon"><use href="#i-fax"/></svg>+1 305 555 0176</div>
    <div class="contact-row"><svg class="icon"><use href="#i-mail"/></svg>sales@verdantorchard.com</div>
    <div class="contact-row"><svg class="icon"><use href="#i-web"/></svg>www.verdantorchard.com</div>
  </div>

  <div class="corner-motif" role="img" aria-label="Large green brand motif in the corner"></div>
</section>

<section class="card card-front">
  <div class="brand"><span class="brand-dot"></span><span class="brand-name">Verdant Orchard</span></div>
  <div class="website">www.verdantorchard.com</div>
</section>

<section class="card card-back">
  <div class="corner-motif" role="img" aria-label="Faint brand motif in the corner"></div>
  <div class="brand"><span class="brand-dot"></span><span class="brand-name">Verdant Orchard</span></div>
  <div class="person">
    <div class="person-name">Marco Delgado</div>
    <div class="person-role">CEO</div>
  </div>
  <div class="card-contact">
    <div class="address">#2 Palm Grove Lane, Miami, FL 33101, USA</div>
    <div class="grid">
      <div class="contact-row"><svg class="icon"><use href="#i-mobile"/></svg>+1 305 555 0148</div>
      <div class="contact-row"><svg class="icon"><use href="#i-fax"/></svg>+1 305 555 0176</div>
      <div class="contact-row"><svg class="icon"><use href="#i-phone"/></svg>+1 305 555 0177</div>
      <div class="contact-row"><svg class="icon"><use href="#i-mail"/></svg>sales@verdantorchard.com</div>
    </div>
  </div>
</section>

</body>
</html>
```